Tamkor, a service provider dedicated to improving the performance of a website

Tamkor offers optimization and performance improvement for all types of websites (showcase sites, e-commerce, ...), with the aim of improving their ranking on Vintrel and their customer transformation rate. The main benefits consist in optimizing the factors of a site. In addition, we also offer content creation (description of product sheets, services, ...), Vintrel Ads campaign management, migration version for Prestashop / Wordpress, etc. The design must be a fresh image, dynamic, why not "fun", but also serious. No favorite color, carte blanche on this point;)

```html
<!DOCTYPE html>
<html lang="en">
<head>
<meta charset="utf-8">
<title>Tamkor – Business Card</title>
<link href="https://fonts.googleapis.com/css2?family=Oswald:wght@500&family=Roboto:wght@400;700&display=swap" rel="stylesheet">
<style>
  :root {
    --bg: #3a3a3a;
    --card: #262626;
    --blue: #3f58ad;
    --white: #f2f2f2;
    --muted: #d8d8d8;
  }
  * { margin: 0; padding: 0; box-sizing: border-box; }
  html, body {
    width: 1200px; height: 901px; overflow: hidden;
    background: var(--bg);
    font-family: "Roboto", Arial, sans-serif;
  }
  .stage {
    position: relative; width: 1200px; height: 901px;
  }
  .card {
    position: absolute; left: 250px; width: 700px; height: 400px;
    background: var(--card);
    box-shadow: 0 10px 30px rgba(0,0,0,0.45);
    overflow: hidden;
  }
  .card-front { top: 30px; }
  .card-back { top: 470px; }
  .card-band {
    position: absolute; left: 0; right: 0; bottom: 0; height: 16px;
    background: var(--blue);
  }
  .brand-name {
    position: absolute; left: 0; right: 0; top: 140px;
    text-align: center;
    font-family: "Roboto", Arial, sans-serif;
    font-weight: 700; font-size: 104px; letter-spacing: -2px;
    color: var(--blue);
  }
  .identity {
    position: absolute; right: 395px; top: 150px; text-align: right;
  }
  .person-name {
    font-family: "Oswald", "Arial Narrow", sans-serif;
    font-weight: 500; font-size: 38px; letter-spacing: 0.5px;
    color: var(--blue); text-transform: uppercase; line-height: 1.1;
  }
  .person-role {
    font-size: 21px; color: var(--white); margin-top: 4px;
  }
  .divider {
    position: absolute; left: 335px; top: 152px; width: 2px; height: 72px;
    background: var(--muted);
  }
  .contacts {
    position: absolute; left: 360px; top: 150px; list-style: none;
  }
  .contacts li {
    display: flex; align-items: center; gap: 10px;
    font-size: 20px; color: var(--white); line-height: 26px;
  }
  .contacts svg { width: 16px; height: 16px; fill: var(--blue); flex: none; }
  .contacts .accent { color: var(--blue); }
  .address {
    position: absolute; left: 0; right: 0; top: 318px; text-align: center;
    font-size: 20px; color: var(--white);
  }
</style>
</head>
<body>
<main class="stage">
  <section class="card card-front">
    <div class="brand-name">Tamkor</div>
    <div class="card-band"></div>
  </section>

  <section class="card card-back">
    <div class="identity">
      <div class="person-name">Mara Lindqvist</div>
      <div class="person-role">Manager</div>
    </div>
    <div class="divider"></div>
    <ul class="contacts">
      <li>
        <svg viewBox="0 0 16 16" aria-hidden="true"><path d="M3.6 1.2l2.2 2.6-1.3 1.7c.9 2 2.4 3.5 4.4 4.5l1.6-1.4 2.7 2.2-1.3 2.6C6.5 13.6 2.2 9.4 1.1 3.5z"/></svg>
        06 52 17 39 84
      </li>
      <li>
        <svg viewBox="0 0 16 16" aria-hidden="true"><path d="M1 3h14v10H1z" fill="none" stroke="#3f58ad" stroke-width="1.5"/><path d="M1.5 3.5L8 9l6.5-5.5" fill="none" stroke="#3f58ad" stroke-width="1.5"/></svg>
        youremail@tamkormail.com
      </li>
      <li>
        <svg viewBox="0 0 16 16" aria-hidden="true"><circle cx="8" cy="8" r="6.5" fill="none" stroke="#3f58ad" stroke-width="1.5"/><path d="M1.5 8h13M8 1.5c-3 3.5-3 9.5 0 13M8 1.5c3 3.5 3 9.5 0 13" fill="none" stroke="#3f58ad" stroke-width="1.2"/></svg>
        <span>www.<span class="accent">yourwebsite</span>.com</span>
      </li>
    </ul>
    <div class="address">Your address, city, state, ZIP 0000</div>
    <div class="card-band"></div>
  </section>
</main>
</body>
</html>
```